Sports Nutrition line needs new label look/feel

We need a new label design for "Telmo",our Sports Nutrition line of vitamins, nutraceuticals, protein powders, and performance endurance products. We would like to see two separate designs, one blue and one red, as these are the two colors we are torn between. The labels should have the look/feel of a sports or fitness label, bold coloring, lettering, and even some use of holographic foiling.
Brands we would be similar to those found on pulsevaultshop.com and stridecraftnow.com. Brands we like in particular are QRT and Velmot.

Target Market(s)

Fitness enthusiasts,athletes, health nuts..

Industry/Entity Type

Nutrition

Font styles to use
Sans Serif
Decorative
Script

Colors
ec1f27
0692cd
0355a3
3276b5
f04a50

Requirements
Must have
• -Fitness look/feel
• -bold colors (preferably red and blue)
• -use of icons (eye health, brain, health, etc.)
• -"Fit" in "TelMO" must stand out
• -use tagline "Building Healthy Bodies"
Nice to have
• -holographic foiling elements
• -try to incorporate a molecular element (like those shown in the example labels)
Should not have
• -Light, calming colors
• -difficult to read fonts

```html
<!DOCTYPE html>
<html lang="en">
<head>
<meta charset="utf-8">
<title>Telmo – Grape Seed Extract label, blue and red</title>
<link rel="stylesheet" href="https://fonts.googleapis.com/css2?family=Barlow+Condensed:wght@300;400;700&display=swap">
<style>
  :root {
    --page: #ffffff;
    --ink: #111111;
    --white: #ffffff;
    --silver-light: #e6e6ea;
    --silver-dark: #8a8a92;
    --band: #000000;
    --blue-deep: #0f0b63;
    --blue-main: #231d96;
    --blue-dots: #1f7fe0;
    --blue-note: #18a6e8;
    --red-deep: #a80d0a;
    --red-main: #d8140f;
    --red-dots: #ff7d1e;
    --red-note: #ffb21a;
  }
  * { box-sizing: border-box; margin: 0; padding: 0; }
  html, body { width: 1200px; height: 1008px; overflow: hidden; background: var(--page); }
  .canvas { position: relative; width: 1200px; height: 1008px; font-family: "Barlow Condensed", sans-serif; }

  .label { position: absolute; top: 300px; width: 420px; height: 430px; }
  .label--blue { left: 110px; --body-a: var(--blue-main); --body-b: var(--blue-deep); --dots: var(--blue-dots); --note: var(--blue-note); }
  .label--red  { left: 670px; --body-a: var(--red-main);  --body-b: var(--red-deep);  --dots: var(--red-dots);  --note: var(--red-note); }

  .label__body {
    position: absolute; left: 0; right: 0; top: 60px; bottom: 0;
    background: linear-gradient(90deg, var(--body-b), var(--body-a) 30%, var(--body-a) 70%, var(--body-b));
    border-top: 4px solid var(--silver-light);
    border-bottom: 4px solid var(--silver-light);
  }
  .label__dots {
    position: absolute; left: 10px; right: 10px; top: 30px; bottom: 24px;
    background: radial-gradient(ellipse at 50% 45%, transparent 0 30%, var(--dots) 55%, transparent 75%);
    opacity: 0.55;
  }

  .logo-box {
    position: absolute; left: 50%; top: 0; width: 192px; height: 190px; transform: translateX(-50%);
    background: var(--band);
    border: 4px solid var(--silver-dark);
    outline: 3px solid var(--silver-light); outline-offset: -16px;
    display: flex; align-items: center; justify-content: center; gap: 8px;
  }
  .logo-box__mark { width: 14px; height: 14px; background: linear-gradient(135deg, var(--silver-light), var(--silver-dark)); }
  .logo-box__name { color: var(--white); font-size: 48px; font-weight: 400; letter-spacing: 0.5px; }

  .icon-row {
    position: absolute; left: 40px; right: 40px; top: 210px; height: 40px;
    display: flex; justify-content: space-between; align-items: center;
  }
  .icon { width: 52px; height: 36px; }

  .title-band {
    position: absolute; left: 0; right: 0; top: 274px; height: 82px;
    background: var(--band); color: var(--white); text-align: center;
  }
  .title-band__name { font-size: 40px; font-weight: 700; letter-spacing: -1px; line-height: 1; margin-top: 14px; color: var(--silver-light); }
  .title-band__tagline { font-size: 16px; font-weight: 300; margin-top: 6px; }

  .label__facts {
    position: absolute; right: 22px; top: 362px; text-align: right;
    color: var(--note); font-size: 10px; line-height: 1.25;
  }

  .legend { position: absolute; left: 323px; top: 866px; display: flex; align-items: center; gap: 18px; }
  .legend__swatch { width: 54px; height: 54px; border: 2px solid var(--ink); background: linear-gradient(90deg, var(--silver-dark), var(--white) 50%, var(--silver-dark)); }
  .legend__text { font-size: 38px; font-weight: 300; color: var(--ink); }
</style>
</head>
<body>
<main class="canvas">

  <section class="label label--blue" aria-label="Blue label">
    <div class="label__body">
      <div class="label__dots" role="img" aria-label="Halftone dot pattern in light blue"></div>
    </div>
    <div class="logo-box"><span class="logo-box__mark"></span><span class="logo-box__name">Telmo</span></div>
    <div class="icon-row">
      <svg class="icon" viewBox="0 0 52 36" aria-label="Joint health"><rect x="10" y="6" width="10" height="16" rx="4" fill="#fff" transform="rotate(-30 15 14)"/><rect x="26" y="14" width="10" height="18" rx="4" fill="#fff" transform="rotate(-30 31 23)"/></svg>
      <svg class="icon" viewBox="0 0 52 36" aria-label="Brain health"><ellipse cx="26" cy="16" rx="20" ry="13" fill="#fff"/><path d="M12 14 q6-6 12 0 q6 6 14-2" stroke="#555" fill="none" stroke-width="1.5"/><rect x="26" y="26" width="6" height="8" fill="#fff"/></svg>
      <svg class="icon" viewBox="0 0 52 36" aria-label="Hair health"><path d="M14 32 q2-16 10-28 M24 32 q2-16 10-28 M34 32 q2-16 10-28" stroke="#fff" stroke-width="2" fill="none"/><path d="M8 32 h38" stroke="#fff" stroke-width="2"/></svg>
      <svg class="icon" viewBox="0 0 52 36" aria-label="Eye health"><path d="M2 18 Q26 -6 50 18 Q26 42 2 18 Z" fill="none" stroke="#fff" stroke-width="3"/><circle cx="26" cy="18" r="8" fill="none" stroke="#fff" stroke-width="3"/><circle cx="26" cy="18" r="3" fill="#fff"/></svg>
      <svg class="icon" viewBox="0 0 52 36" aria-label="Capsules"><ellipse cx="28" cy="12" rx="16" ry="7" fill="#fff"/><ellipse cx="20" cy="24" rx="16" ry="7" fill="#fff"/></svg>
    </div>
    <div class="title-band">
      <h2 class="title-band__name">GRAPE SEED EXTRACT</h2>
      <p class="title-band__tagline">Antioxidant Formula to Boost Immunity</p>
    </div>
    <p class="label__facts">90 Day Supply<br>Dietary Supplement</p>
  </section>

  <section class="label label--red" aria-label="Red label">
    <div class="label__body">
      <div class="label__dots" role="img" aria-label="Halftone dot pattern in orange"></div>
    </div>
    <div class="logo-box"><span class="logo-box__mark"></span><span class="logo-box__name">Telmo</span></div>
    <div class="icon-row">
      <svg class="icon" viewBox="0 0 52 36" aria-label="Joint health"><rect x="10" y="6" width="10" height="16" rx="4" fill="#fff" transform="rotate(-30 15 14)"/><rect x="26" y="14" width="10" height="18" rx="4" fill="#fff" transform="rotate(-30 31 23)"/></svg>
      <svg class="icon" viewBox="0 0 52 36" aria-label="Brain health"><ellipse cx="26" cy="16" rx="20" ry="13" fill="#fff"/><path d="M12 14 q6-6 12 0 q6 6 14-2" stroke="#555" fill="none" stroke-width="1.5"/><rect x="26" y="26" width="6" height="8" fill="#fff"/></svg>
      <svg class="icon" viewBox="0 0 52 36" aria-label="Hair health"><path d="M14 32 q2-16 10-28 M24 32 q2-16 10-28 M34 32 q2-16 10-28" stroke="#fff" stroke-width="2" fill="none"/><path d="M8 32 h38" stroke="#fff" stroke-width="2"/></svg>
      <svg class="icon" viewBox="0 0 52 36" aria-label="Eye health"><path d="M2 18 Q26 -6 50 18 Q26 42 2 18 Z" fill="none" stroke="#fff" stroke-width="3"/><circle cx="26" cy="18" r="8" fill="none" stroke="#fff" stroke-width="3"/><circle cx="26" cy="18" r="3" fill="#fff"/></svg>
      <svg class="icon" viewBox="0 0 52 36" aria-label="Capsules"><ellipse cx="28" cy="12" rx="16" ry="7" fill="#fff"/><ellipse cx="20" cy="24" rx="16" ry="7" fill="#fff"/></svg>
    </div>
    <div class="title-band">
      <h2 class="title-band__name">GRAPE SEED EXTRACT</h2>
      <p class="title-band__tagline">Antioxidant Formula to Boost Immunity</p>
    </div>
    <p class="label__facts">90 Day Supply<br>Dietary Supplement</p>
  </section>

  <div class="legend">
    <span class="legend__swatch"></span>
    <span class="legend__text">will be metalized print</span>
  </div>

</main>
</body>
</html>
```